Alberta, Canada based Environmental Oilfield Consultant need a Business Card Design

We need a business card design for a year old company based in Edmonton, Alberta, Canada called Ferncrest Consulting Inc. We are environmental consultants primarily for oilfield based companies (pipeline cleanup, site consultations, environmental site training, and site evaluations).

We like the color blue or green, something very clean and crisp looking.
We don't really care if there is an otter on it but most of our work is land based and nothing really to do with oceans or larger bodies of water.

The name Ferncrest was the name of our fathers boat, and named our company that in his memory.

```html
<!DOCTYPE html>
<html lang="en">
<head>
<meta charset="utf-8">
<title>Ferncrest Consulting – Business Card</title>
<link href="https://fonts.googleapis.com/css2?family=Exo+2:wght@400;500;700&display=swap" rel="stylesheet">
<style>
  :root {
    --page-bg: #e9ecef;
    --card-bg: #ffffff;
    --brand-blue: #2f86c9;
    --band-deep: #3a40b2;
    --band-bright: #1c95e6;
    --accent-teal: #5fb8bf;
    --ink: #3a3d42;
    --ink-soft: #5a5e64;
    --rule: #8a8e94;
    --icon-bg: #3b3e44;
  }
  * { margin: 0; padding: 0; box-sizing: border-box; }
  html, body {
    width: 1200px; height: 901px; overflow: hidden;
    background: var(--page-bg);
    font-family: "Exo 2", sans-serif;
  }
  .business-card {
    position: absolute; left: 100px; top: 165px;
    width: 1000px; height: 570px;
    background: var(--card-bg);
    border-radius: 42px;
    overflow: hidden;
    box-shadow: 0 18px 40px rgba(0,0,0,.18);
  }
  .card-art { position: absolute; inset: 0; }
  .wordmark {
    position: absolute; left: 130px; top: 78px;
    font-weight: 700; font-size: 84px; letter-spacing: -1px;
    color: var(--brand-blue); white-space: nowrap;
  }
  .person {
    position: absolute; right: 470px; top: 262px;
    text-align: right; color: var(--ink);
    font-variant: small-caps; letter-spacing: 2px;
  }
  .person-name { font-size: 27px; font-weight: 500; }
  .person-title { font-size: 21px; color: var(--ink-soft); margin-top: 2px; }
  .person-address { font-size: 23px; line-height: 1.35; margin-top: 26px; }
  .divider {
    position: absolute; left: 548px; top: 275px;
    width: 2px; height: 180px; background: var(--rule);
  }
  .contact-list {
    position: absolute; left: 568px; top: 272px;
    list-style: none; color: var(--ink);
    font-variant: small-caps; font-size: 24px; letter-spacing: 2px;
  }
  .contact-list li { display: flex; align-items: center; gap: 10px; height: 33px; }
  .contact-list li.gap { margin-top: 8px; }
  .contact-icon { width: 20px; height: 20px; flex: none; }
</style>
</head>
<body>
<div class="business-card">
  <svg class="card-art" viewBox="0 0 1000 570" width="1000" height="570" aria-hidden="true">
    <defs>
      <linearGradient id="bandFill" x1="0" y1="0" x2="1" y2="0">
        <stop offset="0" stop-color="var(--band-deep)"/>
        <stop offset="0.55" stop-color="var(--band-bright)"/>
        <stop offset="1" stop-color="var(--band-deep)"/>
      </linearGradient>
      <path id="sitePath" d="M150 468 C 300 500, 440 528, 620 552"/>
    </defs>
    <path d="M0 340 C 250 430, 600 505, 1000 538 L1000 570 L0 570 Z" fill="url(#bandFill)"/>
    <path d="M0 300 C 260 405, 620 483, 1000 520" fill="none" stroke="var(--accent-teal)" stroke-width="13"/>
    <text font-family="Exo 2, sans-serif" font-size="23" letter-spacing="4" fill="#ffffff">
      <textPath href="#sitePath">www.ferncrestconsult.ca</textPath>
    </text>
  </svg>

  <div class="wordmark">Ferncrest Consulting</div>

  <div class="person">
    <div class="person-name">Daniel Hart</div>
    <div class="person-title">Owner / C.E.O</div>
    <div class="person-address">Suite # 410, Elm Bldg,<br>AB T5J 2R4</div>
  </div>

  <div class="divider"></div>

  <ul class="contact-list">
    <li>
      <svg class="contact-icon" viewBox="0 0 20 20" aria-label="Phone"><circle cx="10" cy="10" r="10" fill="var(--icon-bg)"/><path d="M6 5 l2 0 1 3 -1.5 1 a7 7 0 0 0 3.5 3.5 l1 -1.5 3 1 0 2 a1 1 0 0 1 -1 1 a9 9 0 0 1 -8 -8 a1 1 0 0 1 1 -1z" fill="#fff"/></svg>
      780-555-0142
    </li>
    <li>
      <svg class="contact-icon" viewBox="0 0 20 20" aria-label="Mobile"><circle cx="10" cy="10" r="10" fill="var(--icon-bg)"/><rect x="7" y="4" width="6" height="12" rx="1" fill="#fff"/><rect x="8" y="5.5" width="4" height="7" fill="var(--icon-bg)"/></svg>
      780-555-0187
    </li>
    <li>
      <svg class="contact-icon" viewBox="0 0 20 20" aria-label="Fax"><circle cx="10" cy="10" r="10" fill="var(--icon-bg)"/><rect x="5" y="8" width="10" height="6" rx="1" fill="#fff"/><rect x="7" y="5" width="6" height="3" fill="#fff"/></svg>
      780-555-0163
    </li>
    <li class="gap">
      <svg class="contact-icon" viewBox="0 0 20 20" aria-label="Email"><circle cx="10" cy="10" r="10" fill="var(--icon-bg)"/><rect x="5" y="6.5" width="10" height="7" fill="#fff"/><path d="M5 6.5 L10 10.5 L15 6.5" fill="none" stroke="var(--icon-bg)" stroke-width="1"/></svg>
      info@ferncrestmail.com
    </li>
    <li>
      <svg class="contact-icon" viewBox="0 0 20 20" aria-label="Website"><circle cx="10" cy="10" r="10" fill="var(--icon-bg)"/><g fill="none" stroke="#fff" stroke-width="1.2"><circle cx="10" cy="10" r="5.5"/><ellipse cx="10" cy="10" rx="2.3" ry="5.5"/><path d="M4.5 10 H15.5"/></g></svg>
      www.ferncrestsite.com
    </li>
  </ul>
</div>
</body>
</html>
```